Name of company is Bluebird Meadow Shear Sharpening and Sales.Card design basic idea; I'm thinking back side just showing a sharp BLUEBIRD MEADOW. Front side: I'm thinking a tiger showing teeth and claws.With the words "Bluebird Meadow" larger type emphasized on one line.Then "Shear Sharpening and Sales" on the next line.Other info on front of card should be my name and phone #'s and address: Marcus Pellingham P (407)555-0174 CP (321)555-0138 My address is NOT to be emphasized.Can go at bottom of card. It is: 5127 Brennigan Lane Orlando FL 32899 If all that's too much to fit without looking cluttered than maybe the claw on the front with all the contact info. and just the Tiger on back of card. Whichever looks best.

Target Market(s)

Beauty Salons

Industry/Entity Type

It Company

Contact Information for Business Card

The 2 images,the claw and the tiger,could be either illustrations or photos.Whatever looks best.Got to be eye grabbing either way.

Requirements
Must have
• Contact info. Must be in color. And emphasize the identity. BLUEBIRD MEADOW.Tiger on one side.Showing TEETH. Bluebird Meadow on the other side. Showing the CLAW. .Both pics must emphasize SHARPNESS...This is a shear SHARPENING business. If one of the claw pics shows cutting grooves into something that's fine too. Card must show sharpness of the claw blade somehow.
Nice to have
• Attention grabbing. Images should jump off the card!
Should not have
• No boring cuddly tiger pics showing no teeth or claws or dull teeth or claws. No Black and whites.. No extra words other than what I've listed.

```html
<!DOCTYPE html>
<html lang="en">
<head>
<meta charset="utf-8">
<title>Bluebird Meadow — Business Card</title>
<link href="https://fonts.googleapis.com/css2?family=Open+Sans:wght@400;700&family=Oswald:wght@400;600&display=swap" rel="stylesheet">
<style>
  :root {
    --page-bg: #e9e7e4;
    --card-bg: #3a3a3b;
    --card-text: #ffffff;
    --badge-light: #f4f4f4;
    --badge-shade: #d2d2d2;
    --brand-ink: #383838;
    --brand-accent: #f39a1e;
  }
  html, body {
    margin: 0;
    padding: 0;
    width: 1200px;
    height: 900px;
    overflow: hidden;
    background: var(--page-bg);
  }
  .business-card {
    position: absolute;
    left: 100px;
    top: 140px;
    width: 1000px;
    height: 620px;
    background: var(--card-bg);
    box-shadow: 0 6px 18px rgba(0,0,0,0.18);
    font-family: "Open Sans", Arial, sans-serif;
    color: var(--card-text);
    overflow: hidden;
  }
  .holder-name {
    position: absolute;
    left: 55px;
    top: 90px;
    margin: 0;
    font-family: "Oswald", "Open Sans", sans-serif;
    font-weight: 600;
    font-size: 44px;
    letter-spacing: 1.5px;
    line-height: 1.1;
  }
  .contact-list {
    position: absolute;
    left: 55px;
    top: 376px;
    margin: 0;
    padding: 0;
    list-style: none;
    font-size: 26px;
    line-height: 36px;
  }
  .contact-list li {
    display: flex;
    align-items: center;
    gap: 10px;
  }
  .contact-icon {
    width: 20px;
    height: 22px;
    fill: var(--card-text);
  }
  .postal-address {
    position: absolute;
    left: 55px;
    top: 475px;
    margin: 0;
    font-style: normal;
    font-size: 26px;
    line-height: 36px;
  }
  .brand-badge {
    position: absolute;
    left: 448px;
    top: 54px;
    width: 514px;
    height: 514px;
    border-radius: 50%;
    background: radial-gradient(circle at 40% 35%, var(--badge-light), var(--badge-shade));
    display: flex;
    flex-direction: column;
    align-items: center;
    text-align: center;
    font-family: "Oswald", "Open Sans", sans-serif;
  }
  .brand-mark {
    margin-top: 110px;
    width: 150px;
    height: 150px;
    border-radius: 50%;
    background: var(--brand-accent);
  }
  .brand-name {
    margin: 20px 0 0;
    color: var(--brand-ink);
    font-weight: 600;
    font-size: 56px;
    line-height: 1;
    letter-spacing: 1px;
  }
  .brand-tagline {
    margin: 6px 0 0;
    color: var(--brand-accent);
    font-weight: 400;
    font-size: 30px;
    line-height: 1.1;
    letter-spacing: 0.5px;
  }
</style>
</head>
<body>
  <section class="business-card">
    <h1 class="holder-name">MARCUS PELLINGHAM</h1>

    <ul class="contact-list">
      <li>
        <svg class="contact-icon" viewBox="0 0 24 24" aria-hidden="true"><path d="M6.6 10.8c1.4 2.8 3.8 5.1 6.6 6.6l2.2-2.2c.3-.3.7-.4 1-.2 1.1.4 2.3.6 3.6.6.6 0 1 .4 1 1V20c0 .6-.4 1-1 1C10.6 21 3 13.4 3 4c0-.6.4-1 1-1h3.5c.6 0 1 .4 1 1 0 1.3.2 2.5.6 3.6.1.3 0 .7-.2 1L6.6 10.8z"/></svg>
        <span>(407)555-0174</span>
      </li>
      <li>
        <svg class="contact-icon" viewBox="0 0 24 24" aria-hidden="true"><path d="M16 1H8C6.9 1 6 1.9 6 3v18c0 1.1.9 2 2 2h8c1.1 0 2-.9 2-2V3c0-1.1-.9-2-2-2zm0 17H8V4h8v14zm-4 3.5c-.6 0-1-.4-1-1s.4-1 1-1 1 .4 1 1-.4 1-1 1z"/></svg>
        <span>(321)555-0138</span>
      </li>
    </ul>

    <address class="postal-address">5127 Brennigan Lane<br>Orlando FL 32899</address>

    <div class="brand-badge">
      <div class="brand-mark" aria-hidden="true"></div>
      <p class="brand-name">BLUEBIRD MEADOW</p>
      <p class="brand-tagline">SHEAR SHARPENING AND SALES</p>
    </div>
  </section>
</body>
</html>
```